Koveli Seafood Shipping Packaging Re-Design

We need a packaging (Shipping Carton) design for our Seafood Products (FROZEN). We already have a basic packaging design which we prefer to have a modern touch on it.
Spec :
1. It must show our logo (Attached), note that the text of "KOVELI" which accompany the logo is optional, it can be omitted & showing only the logo.
2. Main color is Blue
3. Our carton is regular shipping box with dimension L43cm x W 27cm x H 16cm.
4. Our material of Carton is both Brown & White Kraft Paperboard, so the design should look nice in both material.

Attached our Logo and packaging design.

Target Market(s)

Frozen Seafood Distributor & Seafood Buyer

Industry/Entity Type

Food Production

Requirements
Must have
• 1. Must Show our Logo
• 2. Main Color of the Text/Logo is Blue
• 3. On the side of the packaging / Carton must show two box of CODE & SIZE
• 4. Must Show these icons :
• a. Handle with Care
• b. Maximum Stackable 10 Carton
• c. Recyleable Material
• d. Protect from the Water/Rain
Nice to have
• Would prefer to have a modern design

```html
<!DOCTYPE html>
<html lang="en">
<head>
<meta charset="utf-8">
<title>Koveli Frozen Seafood Shipping Carton – Dieline</title>
<link rel="stylesheet" href="https://fonts.googleapis.com/css2?family=Archivo:wght@600;700&family=Cinzel:wght@500;700&family=Noto+Sans+SC:wght@400&display=swap">
<style>
  :root {
    --stage: #acacac;
    --board: #ffffff;
    --ink: #2f3d9c;
    --ink-deep: #26318a;
    --wave-light: #a9aee0;
    --wave-mid: #6f78c6;
    --line: #3a4cb0;
  }
  html, body {
    margin: 0;
    width: 1200px;
    height: 1200px;
    overflow: hidden;
    background: var(--stage);
  }
  .dieline {
    position: absolute;
    left: 30px;
    top: 480px;
    width: 1140px;
    height: 240px;
    filter: drop-shadow(0 3px 4px rgba(0,0,0,0.25));
  }
  .panel { fill: var(--board); stroke: var(--line); stroke-width: 1; }
  .frame { fill: none; stroke: var(--ink); stroke-width: 1.6; }
  .brand-name {
    font-family: "Cinzel", serif;
    font-weight: 500;
    font-size: 34px;
    fill: var(--ink-deep);
    letter-spacing: 1px;
  }
  .brand-mark { fill: var(--ink-deep); }
  .label-en {
    font-family: "Archivo", Arial, sans-serif;
    font-weight: 700;
    font-size: 10.5px;
    fill: var(--ink);
  }
  .label-cn {
    font-family: "Noto Sans SC", sans-serif;
    font-size: 10.5px;
    fill: var(--ink);
  }
  .icon { fill: none; stroke: var(--ink); stroke-width: 1.3; stroke-linecap: round; stroke-linejoin: round; }
  .icon-fill { fill: var(--ink); }
  .icon-num { font-family: "Archivo", Arial, sans-serif; font-weight: 700; font-size: 8px; fill: var(--ink); }
  .temp-text { font-family: "Archivo", Arial, sans-serif; font-weight: 600; font-size: 5px; fill: #ffffff; }
</style>
</head>
<body>
<svg class="dieline" viewBox="0 0 1140 240" xmlns="http://www.w3.org/2000/svg">
  <defs>
    <linearGradient id="band-top" x1="0" y1="0" x2="0" y2="1">
      <stop offset="0" stop-color="var(--wave-mid)"/>
      <stop offset="1" stop-color="var(--ink)"/>
    </linearGradient>
    <linearGradient id="band-bottom" x1="0" y1="0" x2="0" y2="1">
      <stop offset="0" stop-color="var(--wave-light)"/>
      <stop offset="0.55" stop-color="var(--wave-mid)"/>
      <stop offset="1" stop-color="var(--ink)"/>
    </linearGradient>

    <g id="side-panel-content">
      <!-- handling icons -->
      <rect class="frame" x="13" y="13" width="23" height="23"/>
      <path class="icon" d="M19 21 l5.5 -3 l5.5 3 v5 l-5.5 3 l-5.5 -3 z M19 21 l5.5 3 l5.5 -3 M24.5 24 v5 M16 27 q2 6 8.5 6 q6.5 0 8.5 -6"/>
      <rect class="frame" x="13" y="40" width="23" height="23"/>
      <text class="icon-num" x="24.5" y="48" text-anchor="middle">10</text>
      <path class="icon-fill" d="M18 58 l3 -7 h7 l3 7 z"/>
      <rect class="icon-fill" x="16" y="59" width="17" height="2"/>
      <rect class="frame" x="13" y="68" width="23" height="23"/>
      <path class="icon" d="M20 77 l3 -4 h4 M28 72 l1 4 l-4 0 M31 80 l-2 5 h-4 M22 86 l-3 -1 l2 -3 M18 81 l3 4"/>
      <rect class="frame" x="13" y="95" width="23" height="23"/>
      <path class="icon" d="M16.5 106 q8 -9 16 0 q-4 -2 -8 0 q-4 -2 -8 0 z M24.5 105 v9 q0 2 -2 2 q-2 0 -2 -2"/>
      <!-- code / size boxes -->
      <rect class="frame" x="48" y="14" width="76" height="106"/>
      <line class="frame" x1="48" y1="34" x2="124" y2="34"/>
      <text class="label-en" x="54" y="28">CODE</text>
      <text class="label-cn" x="91" y="28">代码</text>
      <rect class="frame" x="132" y="14" width="75" height="106"/>
      <line class="frame" x1="132" y1="34" x2="207" y2="34"/>
      <text class="label-en" x="138" y="28">SIZE</text>
      <text class="label-cn" x="176" y="28">规格</text>
    </g>

    <g id="brand-lockup">
      <circle class="brand-mark" cx="84" cy="158" r="30"/>
      <text class="brand-name" x="128" y="178">KOVELI</text>
    </g>
  </defs>

  <!-- Main panel: front -->
  <g class="main-panel">
    <rect class="panel" x="0" y="0" width="349" height="240"/>
    <rect x="0" y="0" width="349" height="28" fill="url(#band-top)" role="img" aria-label="Ocean wave pattern band"/>
    <rect class="frame" x="25" y="33" width="105" height="69"/>
    <line class="frame" x1="25" y1="67" x2="130" y2="67"/>
    <!-- frozen -18°C mark -->
    <g class="frozen-mark">
      <path class="icon" d="M280 38 a5 5 0 0 1 10 0 v44 a10 10 0 1 1 -10 0 z"/>
      <circle class="icon-fill" cx="285" cy="91" r="8"/>
      <line class="icon" x1="285" y1="83" x2="285" y2="50"/>
      <text class="temp-text" x="285" y="93" text-anchor="middle">-18°C</text>
      <path class="icon" d="M308 52 v22 M298.5 57.5 l19 11 M298.5 68.5 l19 -11 M305 53 l3 3 l3 -3 M305 73 l3 -3 l3 3"/>
    </g>
    <use href="#brand-lockup"/>
    <rect x="0" y="200" width="349" height="40" fill="url(#band-bottom)" role="img" aria-label="Layered ocean wave pattern"/>
  </g>

  <!-- Side panel -->
  <g class="side-panel" transform="translate(349 110)">
    <rect class="panel" x="0" y="0" width="220" height="130"/>
    <use href="#side-panel-content"/>
  </g>

  <!-- Main panel: back -->
  <g class="main-panel" transform="translate(569 0)">
    <rect class="panel" x="0" y="0" width="351" height="240"/>
    <rect x="0" y="0" width="351" height="28" fill="url(#band-top)" role="img" aria-label="Ocean wave pattern band"/>
    <text class="brand-name" x="175" y="80" text-anchor="middle" style="font-weight:700;font-size:38px">LANHAI</text>
    <use href="#brand-lockup" transform="translate(4 0)"/>
    <rect x="0" y="200" width="351" height="40" fill="url(#band-bottom)" role="img" aria-label="Layered ocean wave pattern"/>
  </g>

  <!-- Side panel -->
  <g class="side-panel" transform="translate(920 110)">
    <rect class="panel" x="0" y="0" width="220" height="130"/>
    <use href="#side-panel-content"/>
  </g>
</svg>
</body>
</html>
```